Dentist Home Page Design

We need a home page design to be used as a responsive wordpress theme for our dentist website. Website overall look and feel should look professional, yet very friendly as going to dentist is not people's favorite thing to do, for most it might even be scary. We want our website to differentiate with its design from all other generic looking cookie cutter dentists and creates a branded feel.
you can use a generic image for the 680x300px banner on the home pageif you like in the meantime). Total width should not exceed 960 px
Please follow the layout on the wireframes, do not add or delete random elements.
Target Market(s)
mostly targets male/female between 30-45, families with kids as well.
Industry/Entity Type
It Professional
Colors
Designer to choose colors to be used in the design.
Look and feel
Each slider illustrates characteristics of the customer's brand and the style your logo design should communicate.

```html
<!DOCTYPE html>
<html lang="en">
<head>
<meta charset="utf-8">
<title>Harbourview Dental – Home</title>
<link href="https://fonts.googleapis.com/css2?family=Lato:wght@400;700&display=swap" rel="stylesheet">
<style>
:root{
  --blue:#0b5cb3;
  --blue-dark:#1b4b94;
  --blue-deep:#153a73;
  --blue-bar:#1e4d97;
  --blue-text:#1d5fb0;
  --sky:#dcedf9;
  --orange:#f47b20;
  --orange-dark:#e0600d;
  --ink:#333;
  --muted:#666;
  --line:#d7dde6;
  --page:#fafbfc;
  --white:#fff;
}
*{box-sizing:border-box;margin:0;padding:0}
html,body{width:695px;height:1200px;overflow:hidden}
body{position:relative;background:var(--page);font-family:"Lato",Arial,sans-serif;color:var(--ink)}
.abs{position:absolute}

/* header */
.site-header{position:absolute;left:0;top:0;width:695px;height:89px;background:var(--white)}
.brand{position:absolute;left:92px;top:24px;display:flex;align-items:center;gap:5px;font-weight:700;font-size:17px;line-height:17px;color:var(--blue-deep);width:80px}
.brand-dot{width:9px;height:9px;border-radius:50%;background:#d8262e;flex:none}
.doctor-card{position:absolute;left:182px;top:22px;width:166px;height:48px;border-top:1px solid #f2c29d;border-bottom:1px solid #f2c29d;display:flex;flex-direction:column;justify-content:center;align-items:center}
.doctor-card .name{font-size:13px;font-weight:400;color:var(--blue-deep);letter-spacing:.5px}
.doctor-card .role{font-size:6.5px;color:var(--blue-text);margin-top:3px}
.social-top{position:absolute;left:502px;top:8px;display:flex;gap:10px}
.social-top span{width:17px;height:17px;border-radius:50%;background:#bdbdbd}
.phone-big{position:absolute;right:97px;top:30px;font-size:19px;color:var(--blue-text);font-weight:400}
.btn{position:absolute;display:flex;align-items:center;justify-content:center;text-align:center;color:var(--white);font-size:6.8px;line-height:7px;border-radius:3px;background:linear-gradient(var(--orange),var(--orange-dark));border:1px solid #d45a10}
.btn-call{left:472px;top:58px;width:58px;height:21px}
.btn-consult{left:540px;top:58px;width:59px;height:21px}

/* nav */
.main-nav{position:absolute;left:0;top:89px;width:695px;height:29px;background:linear-gradient(#5a86c6,#2f62ad);border-top:1px solid #9bb5dc}
.main-nav ul{list-style:none;position:absolute;left:104px;width:489px;top:0;height:28px;display:flex;justify-content:space-between;align-items:center}
.main-nav li{font-size:8.6px;color:var(--white);font-weight:700}

/* hero */
.hero{position:absolute;left:0;top:118px;width:695px;height:246px;background:var(--blue)}
.hero-photo{position:absolute;left:91px;top:15px;width:348px;height:208px;background:linear-gradient(135deg,#e9e4df,#c99e86 55%,#8a6d5c)}
.booking{position:absolute;left:446px;top:15px;width:158px;height:208px;background:var(--sky)}
.booking-head{height:24px;background:var(--blue-dark);color:var(--white);font-size:9.6px;display:flex;align-items:center;padding-left:14px;gap:5px;position:relative}
.booking-head svg{flex:none}
.booking-head::after{content:"";position:absolute;right:-1px;top:0;border-top:24px solid var(--blue);border-left:8px solid transparent;}
.field{position:absolute;left:14px;width:130px;height:18px;background:var(--white);border:1px solid #cfd9e3;font-size:6.4px;color:#999;padding-left:6px;display:flex;align-items:center}
.field .caret{position:absolute;right:0;top:0;width:18px;height:16px;border-left:1px solid #cfd9e3;display:flex;align-items:center;justify-content:center}
.btn-submit{left:48px;top:172px;width:60px;height:21px;font-size:8.5px}

/* intro */
.intro-title{position:absolute;left:91px;top:384px;font-size:13.6px;font-weight:400;color:#222}
.intro-text{position:absolute;left:91px;width:296px;font-size:6.6px;line-height:11.5px;color:#555}
.video{position:absolute;left:396px;top:386px;width:206px;height:157px;background:linear-gradient(135deg,#cfe6f7,#6fb1e2 60%,#3d8ed0)}
.video-bar{position:absolute;left:0;bottom:0;width:100%;height:17px;background:#1e1e1e}
.video-progress{position:absolute;left:0;top:0;height:3px;width:100%;background:#555}
.video-progress i{display:block;width:18%;height:3px;background:#d42a1f}
.video-time{position:absolute;left:46px;top:6px;font-size:6px;color:#ddd}

/* section bars */
.bar{position:absolute;height:20px;background:var(--blue-bar);color:var(--white);font-size:7.2px;font-weight:700;display:flex;align-items:center;padding-left:9px;border-bottom:2px solid #153a73}
.bar-center{justify-content:center;padding-left:0}
.bar-center::after{content:"";position:absolute;left:50%;bottom:-6px;margin-left:-5px;border-top:5px solid var(--blue-bar);border-left:5px solid transparent;border-right:5px solid transparent}

.service{position:absolute;display:flex;align-items:center;gap:5px;font-size:7px;color:#555}
.service .ico{width:14px;height:14px;border-radius:50%;border:1.5px solid var(--blue-text);display:flex;align-items:center;justify-content:center}
.link{position:absolute;font-size:7px;color:#333;text-decoration:underline}

.tile{position:absolute;top:585px;width:98px;height:77px}
.tile-kids{left:396px;background:linear-gradient(#ffffff,#f4d9b8 60%,#e7a85b)}
.tile-doctor{left:504px;background:linear-gradient(135deg,#7aa36a,#c9a58b 50%,#5d6b4e)}

.thumb{position:absolute;width:76px;height:59px;background:linear-gradient(135deg,#cfe6f7,#6fb1e2 60%,#3d8ed0)}
.thumb::after{content:"";position:absolute;left:0;bottom:0;width:100%;height:6px;background:#1e1e1e}

.case{position:absolute;display:flex;gap:11px;align-items:flex-start}
.case .pic{width:32px;height:32px;background:linear-gradient(#f4c4b8,#f6f2ef 50%,#e88f82)}
.case .txt{font-size:7px;line-height:12px;color:#555;margin-top:2px}
.case .txt b{display:block;color:var(--blue-text);font-weight:700}

/* social box */
.social-box{position:absolute;left:90px;top:874px;width:520px;height:66px;background:var(--white)}
.social-box .likes{position:absolute;left:9px;top:9px;font-size:6.8px;color:#333;display:flex;align-items:center;gap:4px}
.social-box .likes i{width:7px;height:7px;background:#3b5998;display:block}
.social-box .follow{position:absolute;right:18px;top:9px;font-size:6.8px;color:#1a3fa0;text-decoration:underline}
.avatars{position:absolute;left:12px;top:25px;display:flex;gap:2px}
.avatars span{width:26.7px;height:27px;background:linear-gradient(#b7b7b7,#6f6f6f)}

/* footer */
.site-footer{position:absolute;left:0;top:952px;width:695px;height:218px;background:var(--blue-dark);color:var(--white)}
.site-footer h3{position:absolute;top:20px;font-size:14px;font-weight:400}
.f-row{position:absolute;left:88px;width:130px;display:flex;justify-content:space-between;font-size:7px;padding-bottom:6px;border-bottom:1px solid #4b73ad}
.f-row.plain{border-bottom:none}
.f-row a{color:var(--white)}
.addr{position:absolute;left:266px;font-size:7px}
.map{position:absolute;left:266px;top:120px;width:118px;height:74px;background:linear-gradient(135deg,#e9ecde,#dfe5c8 55%,#9fc1e3 70%,#7fb0df)}
.news-sub{position:absolute;left:443px;top:51px;font-size:7px;font-weight:700}
.news-field{position:absolute;left:441px;width:159px;height:19px;background:var(--white);font-size:6.8px;color:#999;display:flex;align-items:center;padding-left:7px}
.btn-signup{left:542px;top:174px;width:58px;height:20px;font-size:8.5px}
.bottom-bar{position:absolute;left:0;top:1170px;width:695px;height:30px;background:var(--blue-deep)}
.social-bottom{position:absolute;left:86px;top:7px;display:flex;gap:9px}
.social-bottom span{width:17px;height:17px;border-radius:50%;background:#3c5a8c}
.copyright{position:absolute;right:95px;top:11px;font-size:6.6px;color:var(--white)}
</style>
</head>
<body>

<header class="site-header">
  <div class="brand"><span>Harbourview Dental</span><span class="brand-dot"></span></div>
  <div class="doctor-card">
    <span class="name">Dr. Martin Kowal</span>
    <span class="role">General Dentist · Orthodontics for Adults &amp; Children</span>
  </div>
  <div class="social-top"><span></span><span></span><span></span><span></span></div>
  <div class="phone-big">(555)210-4488</div>
  <div class="btn btn-call">Click to Call</div>
  <div class="btn btn-consult">Request Free<br>Consultation</div>
</header>

<nav class="main-nav">
  <ul>
    <li>Home</li><li>About Us</li><li>Our Service</li><li>Our Technology</li><li>Dental Care</li><li>Case Studies</li><li>New Patients</li><li>Contact</li>
  </ul>
</nav>

<section class="hero">
  <div class="hero-photo" role="img" aria-label="Smiling family of parents and three children"></div>
  <form class="booking">
    <div class="booking-head">
      <svg width="10" height="10" viewBox="0 0 10 10"><rect x="0.5" y="1.5" width="9" height="8" fill="none" stroke="#fff"/><rect x="0.5" y="1.5" width="9" height="2" fill="#fff"/><rect x="2" y="5" width="1.5" height="1.5" fill="#fff"/><rect x="4.5" y="5" width="1.5" height="1.5" fill="#fff"/><rect x="7" y="5" width="1.5" height="1.5" fill="#fff"/></svg>
      Book An Appointment
    </div>
    <div class="field" style="top:56px">Select Service<span class="caret"><svg width="5" height="3"><path d="M0 0h5L2.5 3z" fill="#1d5fb0"/></svg></span></div>
    <div class="field" style="top:80px">Full Name</div>
    <div class="field" style="top:104px">Email</div>
    <div class="field" style="top:128px">Phone</div>
    <div class="field" style="top:152px">Date of Appointment (required)</div>
    <div class="btn btn-submit">Submit</div>
  </form>
</section>

<main>
  <h1 class="intro-title">Your Experience in Dentistry Begins Now!</h1>
  <p class="intro-text" style="top:410px">It is a long established fact that a reader will be distracted by the readable content of a page when looking at its layout. The point of using Lorem Ipsum is that it has a more-or-less normal distribution of letters, as opposed to using 'Content here, content here', making it look like readable English.</p>
  <p class="intro-text" style="top:467px">Lorem ipsum dolor sit amet, consectetur adipisicing elit, sed do eiusmod tempor incididunt ut labore et dolore magna aliqua. Ut enim ad minim veniam, quis nostrud exercitation ullamco laboris nisi ut aliquip ex ea commodo consequat.It is a long established fact that a reader will be distracted by the readable content of a page when looking at its layout. The point of using Lorem Ipsum is that it has a more-or-less normal distribution of letters, as opposed to using 'Content here, content here', making it look like readable English.</p>

  <div class="video" role="img" aria-label="Video still of a dentist with a smiling family in a clinic">
    <div class="video-bar">
      <div class="video-progress"><i></i></div>
      <svg class="abs" style="left:10px;top:6px" width="8" height="8"><path d="M0 0l7 4-7 4z" fill="#bbb"/></svg>
      <svg class="abs" style="left:28px;top:6px" width="10" height="8"><path d="M0 2.5h2.5L5 0v8L2.5 5.5H0z" fill="#bbb"/></svg>
      <span class="video-time">0:02 / 4:17</span>
    </div>
  </div>

  <div class="bar" style="left:92px;top:565px;width:291px">We strive to provide you with a wide range of treatment options:</div>
  <div class="service" style="left:94px;top:594px"><span class="ico"><svg width="6" height="6"><path d="M0.5 3l2 2 3-4" fill="none" stroke="#1d5fb0" stroke-width="1.2"/></svg></span>General Dentistry</div>
  <div class="service" style="left:198px;top:594px"><span class="ico"><svg width="6" height="6"><path d="M0.5 3l2 2 3-4" fill="none" stroke="#1d5fb0" stroke-width="1.2"/></svg></span>General Dentistry</div>
  <div class="service" style="left:297px;top:594px"><span class="ico"><svg width="6" height="6"><path d="M0.5 3l2 2 3-4" fill="none" stroke="#1d5fb0" stroke-width="1.2"/></svg></span>General Dentistry</div>
  <div class="service" style="left:94px;top:616px"><span class="ico"><svg width="6" height="6"><path d="M0.5 3l2 2 3-4" fill="none" stroke="#1d5fb0" stroke-width="1.2"/></svg></span>General Dentistry</div>
  <div class="service" style="left:198px;top:616px"><span class="ico"><svg width="6" height="6"><path d="M0.5 3l2 2 3-4" fill="none" stroke="#1d5fb0" stroke-width="1.2"/></svg></span>General Dentistry</div>
  <div class="service" style="left:297px;top:616px"><span class="ico"><svg width="6" height="6"><path d="M0.5 3l2 2 3-4" fill="none" stroke="#1d5fb0" stroke-width="1.2"/></svg></span>General Dentistry</div>
  <div class="service" style="left:94px;top:639px"><span class="ico"><svg width="6" height="6"><path d="M0.5 3l2 2 3-4" fill="none" stroke="#1d5fb0" stroke-width="1.2"/></svg></span>General Dentistry</div>
  <div class="service" style="left:198px;top:639px"><span class="ico"><svg width="6" height="6"><path d="M0.5 3l2 2 3-4" fill="none" stroke="#1d5fb0" stroke-width="1.2"/></svg></span>General Dentistry</div>
  <div class="service" style="left:297px;top:639px"><span class="ico"><svg width="6" height="6"><path d="M0.5 3l2 2 3-4" fill="none" stroke="#1d5fb0" stroke-width="1.2"/></svg></span>General Dentistry</div>
  <a class="link" style="left:94px;top:665px">View All Services</a>

  <div class="bar bar-center" style="left:396px;top:565px;width:98px;z-index:2">Dentistry for Kids</div>
  <div class="tile tile-kids" role="img" aria-label="Cheering children with raised arms"></div>
  <div class="bar bar-center" style="left:504px;top:565px;width:98px;z-index:2">Meet Dr. Martin Kowal</div>
  <div class="tile tile-doctor" role="img" aria-label="Portrait of the dentist outdoors"></div>

  <div class="bar" style="left:92px;top:696px;width:291px">Dental Education Videos</div>
  <div class="thumb" style="left:91px;top:729px" role="img" aria-label="Dental education video still"></div>
  <div class="thumb" style="left:197px;top:729px" role="img" aria-label="Dental education video still"></div>
  <div class="thumb" style="left:298px;top:729px" role="img" aria-label="Dental education video still"></div>
  <div class="thumb" style="left:91px;top:799px" role="img" aria-label="Dental education video still"></div>
  <div class="thumb" style="left:197px;top:799px" role="img" aria-label="Dental education video still"></div>
  <div class="thumb" style="left:298px;top:799px" role="img" aria-label="Dental education video still"></div>

  <div class="bar" style="left:396px;top:696px;width:206px">Patient Case Studies</div>
  <div class="case" style="left:396px;top:730px"><span class="pic" role="img" aria-label="Close-up of a smile"></span><span class="txt">Case Study #1:<b>Overbite</b></span></div>
  <div class="case" style="left:505px;top:730px"><span class="pic" role="img" aria-label="Close-up of a smile"></span><span class="txt">Case Study #1:<b>Overbite</b></span></div>
  <div class="case" style="left:396px;top:778px"><span class="pic" role="img" aria-label="Close-up of a smile"></span><span class="txt">Case Study #1:<b>Overbite</b></span></div>
  <div class="case" style="left:505px;top:778px"><span class="pic" role="img" aria-label="Close-up of a smile"></span><span class="txt">Case Study #1:<b>Overbite</b></span></div>
  <div class="case" style="left:396px;top:827px"><span class="pic" role="img" aria-label="Close-up of a smile"></span><span class="txt">Case Study #1:<b>Overbite</b></span></div>
  <div class="case" style="left:505px;top:827px"><span class="pic" role="img" aria-label="Close-up of a smile"></span><span class="txt">Case Study #1:<b>Overbite</b></span></div>

  <div class="social-box">
    <div class="likes"><i></i><span><u>Chris Dalton</u>, <u>Sam Reyes</u> and 2,904,577 others like this.</span></div>
    <a class="follow">Follow Us on Our Page</a>
    <div class="avatars" role="img" aria-label="Profile pictures of followers">
      <span></span><span></span><span></span><span></span><span></span><span></span><span></span><span></span><span></span><span></span><span></span><span></span><span></span><span></span><span></span><span></span><span></span>
    </div>
  </div>
</main>

<footer class="site-footer">
  <h3 style="left:88px">Contact Info and Hours</h3>
  <div class="f-row" style="top:51px"><span>Phone</span><span>(555) 301.2200</span></div>
  <div class="f-row" style="top:76px"><span>Fax</span><span>(555)301.2201</span></div>
  <div class="f-row plain" style="top:100px"><a><u>Email Us</u></a><a><u>Request Appointment</u></a></div>
  <div class="f-row" style="top:142px"><span>Monday - Friday</span><span>8:00 am - Late</span></div>
  <div class="f-row" style="top:166px"><span>Saturday</span><span>8:00 am - 12:00 pm</span></div>
  <div class="f-row plain" style="top:190px"><span>Sunday</span><span>Closed</span></div>

  <h3 style="left:267px">Address &amp; Direction</h3>
  <div class="addr" style="top:51px;font-weight:700">Harbourview Dental</div>
  <div class="addr" style="top:68px">240 Harbour Street East,</div>
  <div class="addr" style="top:84px">Lakeside, ON K0A 1B0</div>
  <div class="addr" style="top:100px">(Free Parking at the Front)</div>
  <div class="map" role="img" aria-label="Street map showing the clinic location"></div>

  <h3 style="left:439px">Sign up for our Newsletter</h3>
  <div class="news-sub">To receive free dental tips from Dr. Martin Kowal</div>
  <div class="news-field" style="top:67px">Name</div>
  <div class="news-field" style="top:100px">Email</div>
  <div class="news-field" style="top:136px">Mobile Phone</div>
  <div class="btn btn-signup">Sign Up</div>
</footer>

<div class="bottom-bar">
  <div class="social-bottom"><span></span><span></span><span></span><span></span></div>
  <div class="copyright">Copyright 2014 Dental Site &nbsp;|&nbsp; All Rights Reserved &nbsp;|&nbsp; Privacy Policy &nbsp;|&nbsp; Site Map</div>
</div>

</body>
</html>
```